Lead Retrieval and IT EVENT Rental Solutions Internal Advertising

RVT is the world’s leading provider of strategic engagement and activation solutions and has been a key driver of innovation in the meetings, events, association and congress industries since 1987.

I work for the HQ location for RVT based in Geneva Switzerland and we service other office locations globally. In my area of responsibilitiy I rent Lead retrieval and IT solutions and hardware for our on-site congress events across Europe. Some of the congresses are hosted by the Geneva office while others are hosted by other offices. To ensure our other offices across Europe choose our services we need an eye catching marketing brochure that explains the value of using internal IT and lead retrieval solutions.

The first two files attached are the documents that need enhancing and the last document is just a text file highlighting guidelines for RVT brand messaging.

Thanks for your help!

```html
<!DOCTYPE html>
<html lang="en">
<head>
<meta charset="utf-8">
<title>Lead Retrieval Rental Solutions – RVT</title>
<link rel="stylesheet" href="https://fonts.googleapis.com/css2?family=Arimo:ital,wght@0,400;0,700;1,400;1,700&display=swap">
<style>
  :root {
    --frame: #5e5e5e;
    --paper: #ffffff;
    --ink: #1c1c1c;
    --pink: #d4207f;
    --pink-soft: #dd5c9d;
    --white: #ffffff;
  }
  html, body { margin: 0; padding: 0; overflow: hidden; }
  body {
    width: 847px; height: 1200px;
    background: linear-gradient(180deg, #6a6a6a, var(--frame));
    font-family: "Arimo", Arial, sans-serif;
    color: var(--ink);
  }
  .sheet {
    position: absolute; left: 20px; top: 16px;
    width: 807px; height: 1168px;
    background: var(--paper);
    box-sizing: border-box;
    padding: 0 36px;
  }
  .masthead {
    display: flex; align-items: flex-start;
    padding-top: 20px; height: 100px;
    border-bottom: 3px solid var(--pink);
  }
  .brand { width: 230px; margin-top: 2px; }
  .brand-name { font-size: 62px; font-weight: 400; color: var(--ink); letter-spacing: 2px; line-height: 1; }
  .titles { margin-left: 8px; }
  .titles .kicker {
    margin: 2px 0 0; font-size: 22px; font-weight: 700; letter-spacing: 0.3px; text-transform: uppercase;
  }
  .titles .tagline { margin: 4px 0 0; font-size: 31px; color: var(--pink); font-weight: 400; white-space: nowrap; }
  .section-title {
    color: var(--pink); font-style: italic; font-weight: 400;
    font-size: 27px; margin: 30px 0 12px;
  }
  .lede { font-weight: 700; font-size: 14.5px; line-height: 1.6; margin: 0 0 18px; }
  .body-text { font-size: 14.5px; line-height: 1.75; }
  .body-text ul { margin: 0 0 22px; padding-left: 18px; }
  .body-text li { margin-bottom: 10px; }
  .body-text .sub { list-style: none; padding-left: 0; margin: 4px 0 0; }
  .body-text .sub li { margin-bottom: 4px; }
  .value-title { margin-top: 26px; margin-bottom: 8px; }
  .columns { display: flex; gap: 36px; }
  .column { flex: 1; }
  .column h3 { font-size: 13px; font-style: italic; font-weight: 700; margin: 0 0 10px; }
  .tile {
    background: var(--pink-soft); color: var(--white);
    font-size: 9.5px; line-height: 1.3; text-align: center;
    padding: 3px 14px; margin-bottom: 4px;
    min-height: 22px; display: flex; align-items: center; justify-content: center;
  }
</style>
</head>
<body>
  <main class="sheet">
    <header class="masthead">
      <div class="brand">
        <span class="brand-name">RVT</span>
      </div>
      <div class="titles">
        <p class="kicker">Lead Retrieval Rental Solutions</p>
        <h1 class="tagline">Enhance Your Congress Experience</h1>
      </div>
    </header>

    <h2 class="section-title">Solutions Designed for You</h2>
    <p class="lede">Lead Retrieval pricing set to maximize your profit sharing and minimize related operational costs</p>

    <div class="body-text">
      <ul>
        <li>Choose between a Standard and Full-Service solutions package that differs based on the provision of specialists for pre-event and on-site device management.</li>
        <li>Operational costs and suggested resale per solution are further explained in the choose your profitability section.</li>
        <li>Discounted minimal basic set up costs under both rental packages are 800 £ and include pre-event device preparation and marketing and sales order management</li>
      </ul>
      <p class="lede">Comprehensive value-driven solutions for resale to your congress client and congress exhibitors include:</p>
      <ul>
        <li>Symposium Pro-Scanner Solution: Session attendance and time in a session can be tracked by participants with scanning in and out of a session.</li>
        <li>Access Check: Access check scanning allows verification on delegate access to events or services. This means that you can check access as delegates enter the venue from different entrance points or you can verify that delegates have registered for the appropriate additional congress service such as a paid luncheon.
          <ul class="sub">
            <li>• Exhibitor Lead Solutions: Exhibitors can track booth traffic and interest in their products by using either the Smart Lead Capture Solution or the Custom Leads Qualifier Solution.</li>
            <li>a) Smart Lead Capture Solution-Leads and associated qualifying comments from one device or multiple devices can be collected and aggregated into one lead list or separated into multiple lists</li>
            <li>b) Custom Leads Qualifier Solution allows for further qualification of leads with direct real time access to survey creation and results data</li>
          </ul>
        </li>
      </ul>
    </div>

    <h2 class="section-title value-title">Delivering Value to You</h2>
    <section class="columns">
      <div class="column">
        <h3>Helping you build Community</h3>
        <div class="tile">Scalable Solutions to meet congress needs</div>
        <div class="tile">No process management on your part as we manage everything, customer service, and support</div>
        <div class="tile">As easy to implement lucrative generation for you and your congress clients</div>
        <div class="tile">Reporting provides valuable insight on delegate attendance and exhibitor patterns at the congress</div>
      </div>
      <div class="column">
        <h3>Helping You Drive Digital</h3>
        <div class="tile">At no cost RVT and your congress are seen as a smart technology solutions provider</div>
        <div class="tile">Free solutions consultation throughout the process</div>
        <div class="tile">Simple technology with comprehensive training to administer solutions</div>
        <div class="tile">On time delivery of fully functional and pre-configured new generation equipment</div>
      </div>
    </section>
  </main>
</body>
</html>
```